Clean & Inspiring Web Design Project

Larkspur Prototype Studio, LLC (also known as LP-Studio) is a company which provides 3D printing services and products. The emphasis is on making these products and services available to the mass-market - customers and users who may or may not have prior experience with 3D printing and/or rapid prototyping technologies. We are a start-up company, looking to build a clean and creativity inspiring brand - our site must encourage visitor to engage and make something. Our aim is to help take mere ideas and turn them into tangible items. We want to show a fusion of ideas (e.g. pencil sketches on graph paper) with design tools (e.g. CAD and drafting software) and rapid prototyping (e.g. TinkNod 3D printers, Stereolithography Machines, etc.). We would like the website to appear professional but at the same time easy to navigate and a good balance between text and pictures. The final design should inspire customers to nurture their ideas into real products and communicate our services to our customers. Our site should have the feel of a vibrant social community with the added benefit of tangible physical creations.

Target Market(s)

People with great ideas that need to be designed into a real product

Industry/Entity Type

Printing

Requirements
Must have
• - Website design should include 2 layouts - one for a "landing page" and one for a "content page"
- Website design must incorporate attached company logo (or derivative of this logo)
- Website design should incorporate the menu options shown in the attached PDF UI concept (UI does not necessarily need to look like the provided concept, just include all the clickable elements)
- Website design must portray an innovative and cooperative design environment with a look-and-feel that appeals to both amateur and professional designers.
- Please include pictures, illustrations and photographs (as needed) related to 3D printing, CAD design, conventional drafting, engineering and manufacturing industries.
- Design should support scaling to multiple screen sizes, from tablet computers (e.g. Slabix) to very large screen PCs.
- Design should include Username & Password fields for login or a button to pull up a login popup.
Nice to have
• - Website design could include "Invent", "Make", "Produce" and "Buy" options that slowly cycle through - with appropriate photos / graphics. These "menu options" would also be mouse-over enabled to switch into the appropriate context as the cursor enters that region (e.g. mouse over the "Invent" text would bring up page 2, etc.). (See attached Original UI Thoughts)
Should not have
• Requirements - Should Not Have:
- Website design should not portray a service that is very expensive or complicated - we are a reasonably priced service meant to be friendly with amateur inventors
- Website design should not be overly complicated - please keep it reasonably simple
- Website design should not be overly trendy
- Website design should not use more than 2 font styles, gaudy fonts, etc.
- Website design should not be "campy" or "tacky" - playful is ok, but please keep it elegant
- Website design should not be overly masculine or feminine - we will have both women and men as customers

```html
<!DOCTYPE html>
<html lang="en">
<head>
<meta charset="utf-8">
<title>Larkspur Prototype Studio, LLC — Bringing Your Ideas to Market</title>
<link rel="stylesheet" href="https://fonts.googleapis.com/css2?family=Source+Sans+3:wght@200;300;400;600;700&display=swap">
<style>
:root{
  --ink:#1d1d1d;
  --bar-top:#3a3a3a;
  --bar-bottom:#161616;
  --brand:#17679a;
  --brand-dark:#0e5684;
  --brand-light:#3f8ec2;
  --sky:#d2e7f4;
  --orange:#f7a21b;
  --orange-dark:#e58a0c;
  --pink:#e8308a;
  --muted:#5d5d5d;
  --nav-text:#b9b9b9;
  --footer:#c9dde8;
  --white:#ffffff;
}
*{box-sizing:border-box;margin:0;padding:0}
html,body{width:1200px;height:813px;overflow:hidden}
body{font-family:"Source Sans 3",Arial,sans-serif;color:var(--ink);background:var(--white);position:relative}
.abs{position:absolute}

/* top bar */
.topbar{left:0;top:0;width:1200px;height:27px;background:linear-gradient(var(--bar-top),var(--bar-bottom))}
.topnav{left:321px;top:8px;display:flex;gap:16px;font-size:10px;letter-spacing:.2px;color:var(--nav-text);text-transform:uppercase}
.topnav .active{color:var(--orange);position:relative}
.topnav .active::after{content:"";position:absolute;left:50%;top:14px;margin-left:-4px;border:4px solid transparent;border-bottom-color:var(--orange)}
.search-icon{left:554px;top:7px}
.search{left:574px;top:5px;width:181px;height:17px;background:var(--white);border-radius:3px;font-size:8px;color:#888;padding:4px 7px}
.greeting{left:780px;top:8px;font-size:10px;color:var(--nav-text)}
.greeting em{font-style:italic}
.greeting b{color:var(--white);font-weight:600}

/* login */
.login-panel{left:827px;top:28px;width:124px;height:79px;background:linear-gradient(#2a7fb0,var(--brand-dark));border-radius:0 0 4px 4px}
.field{left:7px;width:110px;height:19px;background:linear-gradient(#fff,#e3eef5);border-radius:3px;font-size:8px;color:#666;padding:4px 7px}
.login-btn{left:68px;top:58px;width:49px;height:17px;background:#1c1c1c;border-radius:3px;color:var(--white);font-size:10px;padding:2px 7px}
.login-btn i{position:absolute;right:5px;top:3px;width:11px;height:11px;border-radius:50%;background:var(--orange)}
.login-btn i::after{content:"";position:absolute;left:4px;top:3px;border:3px solid transparent;border-left:4px solid #1c1c1c;border-right:0}

/* hero */
.sky{left:0;top:27px;width:1200px;height:380px;background:linear-gradient(var(--sky),#eef6fb 55%,var(--white))}
.brand-mark{width:58px;height:64px;background:var(--brand);border-radius:6px}
.brand-name{left:374px;top:58px;font-size:27px;color:var(--brand);font-weight:400;letter-spacing:-.2px}
.tagline{left:374px;top:86px;font-size:16px;color:var(--brand-light)}
.hero-photo{left:322px;top:140px;width:280px;height:205px;border-radius:40px;background:radial-gradient(ellipse at 45% 50%,#f4f2ee,#d8d6d0 60%,rgba(255,255,255,0) 75%)}
.arrow{top:215px;width:36px;height:36px;border-radius:4px}
.arrow.prev{left:307px;background:#a3a3a3}
.arrow.next{left:859px;background:#2e2e2e}
.headline{left:622px;top:178px;font-size:54px;font-weight:200;letter-spacing:-1px;line-height:1}
.sub{left:624px;top:228px;font-size:26px;font-weight:300;line-height:1;color:#222}
.sub span{color:var(--pink)}
.sub-small{left:624px;top:254px;font-size:14px;font-weight:300;color:#222}
.dots{left:823px;top:321px;display:flex;gap:7px}
.dots i{width:13px;height:13px;border-radius:50%;background:#555}
.dots i.on{background:var(--brand)}

/* main menu */
.menu-shadow{left:205px;top:398px;width:790px;height:10px;background:radial-gradient(ellipse at 50% 0,rgba(0,0,0,.18),rgba(0,0,0,0) 70%)}
.menu{left:294px;top:357px;width:618px;height:45px;background:linear-gradient(#1d6fa3,var(--brand-dark))}
.home{left:0;top:0;width:54px;height:45px;background:linear-gradient(#ff9a2a,#f07d0a);clip-path:polygon(0 0,40px 0,54px 50%,40px 100%,0 100%)}
.menu-item{top:13px;color:var(--white);font-size:11px;font-weight:600;text-transform:uppercase;line-height:1.05}
.menu-item small{display:block;font-size:7.5px;font-weight:400;text-transform:none;color:#9cc2dc}
.menu-item.current{left:126px;top:5px;width:75px;height:40px;background:var(--white);border-top:3px solid var(--orange);color:var(--ink);text-align:center;padding-top:7px}
.menu-item.current small{color:#888}
.divider{left:428px;top:0;width:1px;height:45px;background:#0a4a73}
.cart-label{left:478px;top:12px;font-size:9px;color:var(--white);line-height:1.2;font-weight:600}
.cart-label b{color:var(--orange)}
.btn{background:linear-gradient(#ffc23c,var(--orange-dark));border:1px solid #d27c08;border-radius:2px;color:#2a1a00;font-size:12px;text-align:center;box-shadow:0 2px 2px rgba(0,0,0,.2)}
.shop-btn{left:519px;top:9px;width:90px;height:27px;padding-top:5px}

/* products */
.product{top:429px;width:150px}
.product-photo{width:150px;height:91px;border:1px solid #cfcfcf;border-radius:3px;box-shadow:0 3px 4px rgba(0,0,0,.15)}
.product h3{margin-top:13px;font-size:12.5px;font-weight:400;color:var(--brand)}
.product p{margin-top:3px;font-size:9px;color:var(--muted);line-height:1.3}
.see-all{left:711px;top:595px;font-size:9px;color:#333}
.more-btn{left:811px;top:585px;width:83px;height:27px;padding-top:5px}

/* footer */
.footer{left:0;top:635px;width:1200px;height:178px;background:var(--footer)}
.f-name{left:374px;top:653px;font-size:16px;color:var(--brand)}
.f-slogan{left:374px;top:673px;font-size:16px;color:var(--brand-light);line-height:1.3}
.follow{left:312px;top:737px;font-size:11px;color:#5f7380}
.socials{left:312px;top:757px;display:flex;gap:6px}
.socials i{width:24px;height:24px;border-radius:3px;background:linear-gradient(#5a5a5a,#222);box-shadow:0 1px 2px rgba(0,0,0,.3)}
.copyright{left:312px;top:792px;font-size:7px;color:#6b7b84}
.f-nav{left:636px;top:656px;font-size:11px;color:#27313a;word-spacing:2px}
.f-photo{left:634px;top:686px;width:116px;height:82px;border:4px solid #eef3f6;outline:1px solid #a9bac3;background:linear-gradient(135deg,#c7b39c,#6d5646 55%,#a08a74)}
.f-title{left:759px;top:685px;font-size:11px;font-weight:600;color:#111}
.f-text{left:759px;top:705px;width:136px;font-size:8.5px;color:#3c4a52;line-height:1.35;text-align:justify}
.read-btn{left:829px;top:743px;width:65px;height:28px;padding-top:6px;font-size:11px}
</style>
</head>
<body>

<header class="abs topbar"></header>
<nav class="abs topnav">
  <span>Why LP</span><span class="active">Dreamer</span><span>Maker</span><span>Producer</span>
</nav>
<svg class="abs search-icon" width="14" height="14" viewBox="0 0 14 14" aria-hidden="true">
  <circle cx="8.5" cy="5.5" r="4" fill="none" stroke="#f7a21b" stroke-width="1.8"/>
  <line x1="5.5" y1="8.5" x2="1.5" y2="12.5" stroke="#f7a21b" stroke-width="2" stroke-linecap="round"/>
</svg>
<div class="abs search">Type search here...</div>
<div class="abs greeting"><em>Hello Guest,</em> <b>Login</b> &nbsp;|&nbsp; Register</div>

<section class="abs sky"></section>

<form class="abs login-panel">
  <div class="abs field" style="top:8px">Username</div>
  <div class="abs field" style="top:34px">Password</div>
  <div class="abs login-btn">Login<i></i></div>
</form>

<div class="abs brand-mark" style="left:309px;top:44px"></div>
<div class="abs brand-name">Larkspur Prototype Studio, LLC®</div>
<div class="abs tagline">Bringing Your Ideas to Market®</div>

<div class="abs hero-photo" role="img" aria-label="Photo of a white 3D-printed cylindrical part with ribbed rings and perforated wall"></div>
<div class="abs arrow prev"><svg width="36" height="36" viewBox="0 0 36 36" aria-hidden="true"><path d="M24 9 L11 18 L24 27 Z" fill="#fff"/></svg></div>
<div class="abs arrow next"><svg width="36" height="36" viewBox="0 0 36 36" aria-hidden="true"><path d="M12 9 L25 18 L12 27 Z" fill="#fff"/></svg></div>
<div class="abs headline">INVENT</div>
<div class="abs sub">Have an <span>idea</span>?</div>
<div class="abs sub-small">We can make it real!</div>
<div class="abs dots"><i class="on"></i><i></i><i></i><i></i></div>

<div class="abs menu-shadow"></div>
<nav class="abs menu">
  <div class="abs home">
    <svg class="abs" style="left:11px;top:11px" width="24" height="22" viewBox="0 0 24 22" aria-hidden="true">
      <path d="M12 1 L23 11 H19.5 V21 H14.5 V15 H9.5 V21 H4.5 V11 H1 Z" fill="#fff"/>
    </svg>
  </div>
  <div class="abs menu-item" style="left:60px">About LP<small>Nam liber tempor</small></div>
  <div class="abs menu-item current">Dream<small>Nobis eleifend</small></div>
  <div class="abs menu-item" style="left:221px">Make<small>Dolor sit amet</small></div>
  <div class="abs menu-item" style="left:290px">Produce<small>Adipiscing consec</small></div>
  <div class="abs menu-item" style="left:376px">Sell<small>Ed delivero</small></div>
  <div class="abs divider"></div>
  <svg class="abs" style="left:440px;top:10px" width="30" height="26" viewBox="0 0 30 26" aria-hidden="true">
    <path d="M1 2 H6 L10 18 H26 L29 6 H8" fill="none" stroke="#cfe0ec" stroke-width="2" stroke-linejoin="round"/>
    <circle cx="12" cy="22.5" r="2.2" fill="#cfe0ec"/><circle cx="24" cy="22.5" r="2.2" fill="#cfe0ec"/>
  </svg>
  <div class="abs cart-label">Shopping<br>Chart <b>(0)</b></div>
  <div class="abs btn shop-btn">Shopping NOW!</div>
</nav>

<main>
  <article class="abs product" style="left:294px">
    <div class="product-photo" role="img" aria-label="Photo of interlocking grey 3D-printed mesh rings" style="background:radial-gradient(ellipse,#9a9a9a,#e6e6e6 55%,#fff 75%)"></div>
    <h3>Product 1</h3><p>Nam liber tempor cum soluta<br>nobis eleifend</p>
  </article>
  <article class="abs product" style="left:450px">
    <div class="product-photo" role="img" aria-label="Photo of a white 3D-printed cylindrical part" style="background:radial-gradient(ellipse,#dcdad4,#f2f1ee 55%,#fff 75%)"></div>
    <h3>Product 1</h3><p>Nam liber tempor cum soluta<br>nobis eleifend</p>
  </article>
  <article class="abs product" style="left:607px">
    <div class="product-photo" role="img" aria-label="Photo of an assortment of colourful printed plastic parts" style="background:radial-gradient(ellipse at 45% 55%,#3a3a3a,#c8563a 40%,#f3f3f3 72%)"></div>
    <h3>Product 1</h3><p>Nam liber tempor cum soluta<br>nobis eleifend</p>
  </article>
  <article class="abs product" style="left:763px">
    <div class="product-photo" role="img" aria-label="Photo of a tan 3D-printed lattice surface" style="background:linear-gradient(135deg,#c9a585,#a67a58 50%,#d9bc9f)"></div>
    <h3>Product 1</h3><p>Nam liber tempor cum soluta<br>nobis eleifend</p>
  </article>
  <div class="abs see-all">Please see our all product</div>
  <div class="abs btn more-btn">Find out more!</div>
</main>

<footer class="abs footer"></footer>
<div class="abs brand-mark" style="left:309px;top:655px"></div>
<div class="abs f-name">Larkspur Prototype Studio, LLC®</div>
<div class="abs f-slogan">What you want...<br>NOW!</div>
<div class="abs follow">Follow Us on</div>
<div class="abs socials"><i></i><i></i><i></i><i></i><i></i></div>
<div class="abs copyright">2012 © Copyright - Larkspur Prototype Studio, LLC</div>
<nav class="abs f-nav">HOME &nbsp;|&nbsp; CONTACT &nbsp;|&nbsp; FRANCHISE &nbsp;|&nbsp; DISTRIBUTORS &nbsp;|&nbsp; CART</nav>
<div class="abs f-photo" role="img" aria-label="Photo of lace-patterned 3D-printed high-heel shoes"></div>
<div class="abs f-title">At vero eos et accusam</div>
<p class="abs f-text">Duis autem vel eum iriure dolor in hendrerit in vulputate velit esse molestie consequat.</p>
<div class="abs btn read-btn">Read more</div>

</body>
</html>
```